Logo and bag for Turkish coffee brand

We are a coffee roasting company. We need a logo for our new Turkish coffee brand. We are targeting C+ to A- customer segment. Our brand is above average in pricing and can be expressed as very good in quality or a bit less than excellentOur brand name is قهواكQahwakIt is an Arabic word that means "Your coffee" and if read in a different way it means "I love You"

Target Market(s)

We are selling in Egyptian market for customer segments from C+ and up to A-

Logo Text

Bunnyar بنّيار

Requirements
Must have
• 1. The logo must contain brand name in Arabic good to have it in Arabic and English if possible.
• 2. All text content must be in Arabic and good to be in both Arabic and English
• 3. The package must include two spaces for limited text paragraphs
• an area for production date and expiry.
• 4. An area for selecting variants of the product. Our coffee has light-medium-dark roasted (فاتح - وسط - غامق)
• Plain or flavored (سادة - محوج)

```html
<!DOCTYPE html>
<html lang="ar">
<head>
<meta charset="utf-8">
<title>بنّيار – Bunnyar Coffee Bag</title>
<link rel="stylesheet" href="https://fonts.googleapis.com/css2?family=Aref+Ruqaa:wght@700&display=swap">
<style>
  :root {
    --stage-blue: #27428a;
    --bag-top: #2a4891;
    --pattern-blue: #2f5aa6;
    --pattern-line: #3d8fd0;
    --label-white: #ffffff;
    --band-blue: #42a1d9;
    --brand-gold: #e2b46a;
    --rule-white: #ffffff;
  }
  html, body {
    margin: 0;
    padding: 0;
    width: 1200px;
    height: 1000px;
    overflow: hidden;
    background: var(--stage-blue);
  }
  .canvas {
    position: relative;
    width: 1200px;
    height: 1000px;
    background: var(--stage-blue);
  }
  .bag-front {
    position: absolute;
    left: 330px;
    top: 88px;
    width: 520px;
    height: 842px;
    background: var(--bag-top);
    border-radius: 14px 14px 6px 6px;
    overflow: hidden;
  }
  .pattern-field {
    position: absolute;
    left: 15px;
    top: 137px;
    width: 490px;
    height: 705px;
    background: linear-gradient(160deg, var(--pattern-line) 0%, var(--pattern-blue) 45%, var(--pattern-line) 100%);
  }
  .variant-band {
    position: absolute;
    left: 160px;
    top: 624px;
    width: 200px;
    height: 218px;
    background: var(--band-blue);
  }
  .variant-grid {
    position: absolute;
    left: 0;
    top: 0;
  }
  .brand-seal {
    position: absolute;
    left: 111px;
    top: 361px;
    width: 296px;
    height: 296px;
    border-radius: 50%;
    background: var(--label-white);
    display: flex;
    flex-direction: column;
    align-items: center;
    justify-content: center;
    gap: 4px;
  }
  .brand-name-ar,
  .brand-name-en {
    font-family: "Aref Ruqaa", serif;
    font-weight: 700;
    color: var(--brand-gold);
    line-height: 1;
  }
  .brand-name-ar {
    font-size: 86px;
    direction: rtl;
  }
  .brand-name-en {
    font-size: 30px;
    letter-spacing: 1px;
  }
</style>
</head>
<body>
  <main class="canvas">
    <section class="bag-front">
      <div class="pattern-field" role="img" aria-label="Blue Islamic geometric star pattern covering the bag front"></div>

      <div class="variant-band">
        <svg class="variant-grid" width="200" height="218" viewBox="0 0 200 218" aria-hidden="true">
          <g stroke="var(--rule-white)" stroke-width="1.5" fill="none">
            <line x1="62" y1="93" x2="62" y2="180"/>
            <line x1="62" y1="120" x2="190" y2="120"/>
            <line x1="62" y1="145" x2="190" y2="145"/>
            <line x1="122" y1="145" x2="122" y2="180"/>
          </g>
        </svg>
      </div>

      <div class="brand-seal">
        <span class="brand-name-ar">بنّيار</span>
        <span class="brand-name-en">Bunnyar</span>
      </div>
    </section>
  </main>
</body>
</html>
```